Verdant Loop Advisors, LLC

I am looking for a simple, clear layout with my logo prominent and embossed, on the best quality card stock available. I would like the business name and phone number included on the card as well......I dont want my name anywhere on the card and I would like my logo embossed on the card......something simple with a white back......open to designs as long as they go along with recycling symbols and green type stuff.....The address, website, cell number, fax number, and email are listed below

5374 Tillbury Fenwood Road
Larkmere, MD 20700

c. 240.555.0143 f. 240.555.0187
e. sales@verdantloopadvisors.example
w. www.verdantloopadvisors.example

Industry/Entity Type

Recycling

```html
<!DOCTYPE html>
<html lang="en">
<head>
<meta charset="utf-8">
<title>Verdant Loop Advisors, LLC — Business Card</title>
<link rel="stylesheet" href="https://fonts.googleapis.com/css2?family=Roboto+Condensed:wght@500;700&display=swap">
<style>
  :root {
    --backdrop: #e4e2de;
    --card-white: #ffffff;
    --card-black: #050605;
    --leaf-green: #2a7a2c;
    --deep-green: #0d2a10;
    --ink: #141414;
    --text-light: #ffffff;
  }
  html, body {
    margin: 0;
    width: 1200px;
    height: 1000px;
    overflow: hidden;
    background: var(--backdrop);
  }
  .canvas {
    position: relative;
    width: 1200px;
    height: 1000px;
  }
  .business-card {
    position: absolute;
    left: 380px;
    top: 115px;
    width: 440px;
    height: 770px;
    overflow: hidden;
    background: var(--card-black);
    box-shadow: 0 10px 30px rgba(0,0,0,0.18);
    font-family: "Roboto Condensed", "Arial Narrow", sans-serif;
  }
  .card-shapes {
    position: absolute;
    inset: 0;
  }
  .brand-lockup {
    position: absolute;
    left: 80px;
    top: 150px;
    display: flex;
    align-items: center;
    gap: 14px;
  }
  .brand-square {
    width: 34px;
    height: 34px;
    background: var(--leaf-green);
  }
  .brand-name {
    margin: 0;
    color: var(--ink);
    font-weight: 700;
    text-transform: uppercase;
    line-height: 1;
  }
  .brand-name .name-main {
    display: block;
    font-size: 32px;
    letter-spacing: 1px;
  }
  .brand-name .name-sub {
    display: block;
    margin-top: 4px;
    font-size: 13px;
    letter-spacing: 6.5px;
  }
  .contact-list {
    position: absolute;
    left: 34px;
    top: 540px;
    margin: 0;
    padding: 0;
    list-style: none;
    color: var(--text-light);
    font-weight: 500;
    font-size: 17px;
    text-transform: uppercase;
    letter-spacing: 0.3px;
  }
  .contact-line {
    display: flex;
    align-items: center;
    height: 29px;
    white-space: nowrap;
  }
  .contact-icon {
    width: 14px;
    height: 14px;
    margin-right: 44px;
    flex: none;
  }
  .contact-icon.blank { visibility: hidden; }
</style>
</head>
<body>
<main class="canvas">
  <article class="business-card">
    <svg class="card-shapes" width="440" height="770" viewBox="0 0 440 770" aria-hidden="true">
      <defs>
        <linearGradient id="greenFade" x1="1" y1="0" x2="0" y2="1">
          <stop offset="0" stop-color="var(--leaf-green)"/>
          <stop offset="0.55" stop-color="var(--deep-green)"/>
          <stop offset="1" stop-color="var(--card-black)"/>
        </linearGradient>
      </defs>
      <circle class="green-disc" cx="470" cy="540" r="420" fill="url(#greenFade)"/>
      <circle class="white-disc" cx="200" cy="-300" r="670" fill="var(--card-white)"/>
    </svg>

    <div class="brand-lockup">
      <span class="brand-square"></span>
      <h1 class="brand-name">
        <span class="name-main">Verdant Loop</span>
        <span class="name-sub">Advisors, LLC</span>
      </h1>
    </div>

    <ul class="contact-list">
      <li class="contact-line">
        <svg class="contact-icon" viewBox="0 0 14 14" aria-label="Address"><path d="M7 1a4 4 0 0 1 4 4c0 3-4 8-4 8S3 8 3 5a4 4 0 0 1 4-4z" fill="#fff"/><circle cx="7" cy="5" r="1.5" fill="#000"/></svg>
        5374 Tillbury Fenwood Road
      </li>
      <li class="contact-line">
        <svg class="contact-icon blank" viewBox="0 0 14 14" aria-hidden="true"></svg>
        Larkmere, MD 20700
      </li>
      <li class="contact-line">
        <svg class="contact-icon" viewBox="0 0 14 14" aria-label="Cell"><path d="M3 1.5l2.2-.5 1.3 3-1.4 1a7 7 0 0 0 3.4 3.4l1-1.4 3 1.3-.5 2.2C11 12.5 1.5 9 3 1.5z" fill="#fff"/></svg>
        240.555.0143
      </li>
      <li class="contact-line">
        <svg class="contact-icon" viewBox="0 0 14 14" aria-label="Fax"><rect x="3" y="1" width="8" height="4" fill="#fff"/><rect x="1" y="5.5" width="12" height="6" rx="1" fill="#fff"/><rect x="3.5" y="9" width="7" height="4" fill="#fff" stroke="#000" stroke-width="0.8"/></svg>
        240.555.0187
      </li>
      <li class="contact-line">
        <svg class="contact-icon" viewBox="0 0 14 14" aria-label="Email"><rect x="1" y="3" width="12" height="8.5" fill="#fff"/><path d="M1 3l6 5 6-5" fill="none" stroke="#000" stroke-width="1"/></svg>
        sales@verdantloopadvisors.example
      </li>
      <li class="contact-line">
        <svg class="contact-icon" viewBox="0 0 14 14" aria-label="Website"><g fill="none" stroke="#fff" stroke-width="1.1"><circle cx="7" cy="7" r="5.5"/><ellipse cx="7" cy="7" rx="2.4" ry="5.5"/><path d="M1.5 7h11M2.5 4h9M2.5 10h9"/></g></svg>
        www.verdantloopadvisors.example
      </li>
    </ul>
  </article>
</main>
</body>
</html>
```